Business Card Design

I'd like to have some business cards designed using my new logo. I am an accountant and company secretary and offer these services through Holloway Meridian Advisory Pty Ltd. I am the sole Director of the company. Please let me know if you require any further logo files.

Industry/Entity Type

Business

```html
<!DOCTYPE html>
<html lang="en">
<head>
<meta charset="utf-8">
<title>Holloway Meridian Advisory – Business Card</title>
<link rel="stylesheet" href="https://fonts.googleapis.com/css2?family=Source+Sans+3:wght@400;700&display=swap">
<style>
  :root {
    --backdrop-light: #e4e5e7;
    --backdrop-dark: #b9bbbe;
    --card-white: #ffffff;
    --brand-blue: #0070bb;
    --brand-blue-deep: #0a5a9c;
    --brand-blue-glow: #1a8fd3;
    --brand-grey: #6d6e71;
    --ink: #1d1d1f;
    --ink-soft: #6d6e71;
  }
  * { margin: 0; padding: 0; box-sizing: border-box; }
  html, body { width: 1200px; height: 1200px; overflow: hidden; }
  body {
    background: radial-gradient(circle at 50% 45%, var(--backdrop-light) 0%, var(--backdrop-dark) 100%);
    position: relative;
    font-family: "Source Sans 3", "Myriad Pro", Arial, sans-serif;
  }
  .card {
    position: absolute;
    left: 216px;
    width: 766px;
    height: 462px;
    overflow: hidden;
    box-shadow: 0 1px 3px rgba(0,0,0,0.15);
  }
  .card--front { top: 126px; background: var(--card-white); }
  .card--back {
    top: 598px;
    height: 462px;
    background: radial-gradient(ellipse 55% 60% at 50% 45%, var(--brand-blue-glow) 0%, var(--brand-blue) 55%, var(--brand-blue-deep) 100%);
  }

  .header-band {
    position: absolute;
    left: 0; right: 0;
    top: 196px;
    height: 8px;
    background: var(--brand-blue);
  }

  .wordmark {
    position: absolute;
    left: 50px;
    top: 60px;
    font-weight: 400;
    color: var(--brand-grey);
    font-size: 24px;
    line-height: 28px;
    letter-spacing: 1px;
    text-transform: uppercase;
  }

  .holder { position: absolute; left: 54px; top: 316px; }
  .holder__name { font-weight: 700; font-size: 20px; color: var(--ink); line-height: 26px; }
  .holder__title { font-size: 18px; color: var(--ink-soft); line-height: 24px; }

  .contact { position: absolute; left: 484px; top: 256px; list-style: none; }
  .contact__item {
    display: flex; align-items: flex-start; gap: 10px;
    font-size: 18px; line-height: 22px; color: var(--ink);
  }
  .contact__item + .contact__item { margin-top: 1px; }
  .contact__item--gap { margin-top: 12px !important; }
  .contact__icon { width: 14px; height: 14px; margin-top: 4px; flex: none; fill: var(--brand-blue); }

  .back-name {
    position: absolute;
    left: 0; right: 0; top: 150px;
    text-align: center;
    font-weight: 400;
    color: var(--card-white);
    font-size: 52px;
    line-height: 62px;
    letter-spacing: 2px;
    text-transform: uppercase;
  }
  .back-web {
    position: absolute; left: 475px; top: 408px;
    display: flex; align-items: center; gap: 8px;
    color: var(--card-white); font-size: 21px;
  }
  .back-web svg { width: 18px; height: 18px; }
</style>
</head>
<body>

<section class="card card--front" aria-label="Business card front">
  <div class="header-band" aria-hidden="true"></div>

  <div class="wordmark">Holloway<br>Meridian Advisory<br>Pty Ltd</div>

  <div class="holder">
    <div class="holder__name">YOUR NAME</div>
    <div class="holder__title">Your title</div>
  </div>

  <ul class="contact">
    <li class="contact__item">
      <svg class="contact__icon" viewBox="0 0 14 14"><path d="M7 1 L1 6.5 H3 V13 H6 V9 H8 V13 H11 V6.5 H13 Z"/></svg>
      <span>Your company address<br>City zipcode</span>
    </li>
    <li class="contact__item contact__item--gap">
      <svg class="contact__icon" viewBox="0 0 14 14"><rect x="4" y="1" width="6" height="12" rx="1"/><rect x="5" y="2.5" width="4" height="5" fill="#fff"/></svg>
      <span>555 555 5555</span>
    </li>
    <li class="contact__item">
      <svg class="contact__icon" viewBox="0 0 14 14"><path d="M3 2 L5.5 4.5 L4.2 6 C5 7.8 6.2 9 8 9.8 L9.5 8.5 L12 11 L10.5 12.6 C6 12 2 8 1.4 3.5 Z"/></svg>
      <span>555 555 5555</span>
    </li>
    <li class="contact__item">
      <svg class="contact__icon" viewBox="0 0 14 14"><rect x="3" y="1" width="8" height="4"/><rect x="1" y="5" width="12" height="6" rx="1"/><rect x="3" y="9" width="8" height="4" fill="#fff" stroke="var(--brand-blue)"/></svg>
      <span>555 555 5555</span>
    </li>
    <li class="contact__item contact__item--gap">
      <svg class="contact__icon" viewBox="0 0 14 14"><rect x="1" y="3" width="12" height="8" rx="1"/><path d="M1.5 3.5 L7 8 L12.5 3.5" fill="none" stroke="#fff" stroke-width="1.2"/></svg>
      <span>email.yourdomain.com</span>
    </li>
    <li class="contact__item">
      <svg class="contact__icon" viewBox="0 0 14 14"><circle cx="7" cy="7" r="6"/><path d="M1 7 H13 M7 1 C4 4 4 10 7 13 M7 1 C10 4 10 10 7 13 M2 4 H12 M2 10 H12" fill="none" stroke="#fff" stroke-width="0.8"/></svg>
      <span>www.yourdomain.com</span>
    </li>
  </ul>
</section>

<section class="card card--back" aria-label="Business card back">
  <div class="back-name">Holloway<br>Meridian Advisory</div>
  <div class="back-web">
    <svg viewBox="0 0 14 14" aria-hidden="true"><circle cx="7" cy="7" r="6" fill="#fff"/><path d="M1 7 H13 M7 1 C4 4 4 10 7 13 M7 1 C10 4 10 10 7 13 M2 4 H12 M2 10 H12" fill="none" stroke="var(--brand-blue)" stroke-width="0.8"/></svg>
    <span>www.yourdomain.com</span>
  </div>
</section>

</body>
</html>
```